Crowdsourced Research Platform: VELTA Polls

VELTA Polls is an acronym for Varied Estimates Linking Topical Attitudes (VELTA) Polls. This is a research effort to format and combine multiple sources of public opinion data from around the world into merged datasets. The website will at first mainly act as a quality control hub and distribution point for official dataset releases. It will provide resources such as codebooks, development guidelines, and instructional videos for crowdsourcing continued expansion of the resource. We need a coded (HTML and CSS) website design and associated files to launch the website with ease. We purchased the domain www.veltapolls.org, but access is blocked while it is under construction.

The website design should be based on a logo recently commissioned (see attached). The design should be simple and professional with lots of white space. We would like the logo on the top left of all pages and the primary navigation menu along the top-right of all pages. The primary navigation menu should have a simple mouse-over effect and the main menu items should expand with secondary drop-down options. The footer should include a few columns with headings and links to different pages. The website layout should be dynamic and expand its width to fit different sized screens. There will be a lot of data and information displayed in tables, so we would like the CSS coding and website design to include tables designed to match the website theme. The main graphical content will be data visualisations such as pie/bar charts, histograms, scatter plots, heat maps, moving average trend lines etc. We would therefore like the design to include modular sections (boxes matching theme to display plots/graphs/etc) that can visually display these types of figures with text/caption underneath to explain the data visualizations.

For more information and written placeholder content, designers should read the attached documents to get a better idea about the project. Some draft working papers using merged datsets have been included for reference and you can use these for their examples of data visualizations and use the written content for filling in page content.

Target Market(s)

The primary target audience will be academics in universities and research institutes. The resource will be most useful to quantitative social scientists, particularly political scientists and sociologists, but any discipline concerned with us humans could find the resource useful. Others such as graduate-level university students, civil servants in government departments, members of research institutions, and policy researchers in non-profit organizations will also find the resource useful.

Coding

Coded - Design and coding required

Number of Pages Required

3 page

Font styles to use
Sans Serif

Colors

Designer to choose colors to be used in the design.

Requirements
Must have
• HTML and CSS coding (not Wordpress)
Nice to have
• Content boxes to display data visualizations alongside articles.

```html
<!DOCTYPE html>
<html lang="en">
<head>
<meta charset="utf-8">
<title>VELTA Polls – Crowdsourced Research</title>
<link href="https://fonts.googleapis.com/css2?family=Arimo:wght@400;500&display=swap" rel="stylesheet">
<style>
  :root {
    --violet: #a05ee0;
    --violet-deep: #9326ee;
    --indigo: #7a66dc;
    --teal: #5fd3c4;
    --mint: #8fe3d6;
    --ink: #222222;
    --muted: #777777;
    --line: #e6e6e6;
    --paper: #ffffff;
    --sand: #b4ab9a;
    --sea: #8d9a9c;
  }
  * { box-sizing: border-box; margin: 0; padding: 0; }
  html, body {
    width: 1200px; height: 589px; overflow: hidden;
    font-family: "Arimo", Arial, sans-serif; color: var(--ink);
  }
  .canvas { position: relative; width: 1200px; height: 589px; overflow: hidden; }
  .backdrop {
    position: absolute; inset: 0;
    background: linear-gradient(90deg, #a862dd 0%, #b38be6 14%, #c5b9ee 45%, #a9dbe3 80%, #80ddd0 100%);
  }
  .top-band {
    position: absolute; left: 150px; top: 0; width: 673px; height: 16px;
    background: linear-gradient(90deg, #7b6fd0, #4fb4c9 60%, #3fd0bd);
  }
  .top-photo {
    position: absolute; left: 823px; top: 0; width: 225px; height: 16px;
    background: linear-gradient(90deg, #d9c6b5, #c9b3a3);
  }
  .sources {
    position: absolute; left: 150px; top: 16px; width: 898px; height: 394px;
    background: var(--paper); text-align: center;
  }
  .eyebrow {
    position: absolute; top: 40px; left: 0; right: 0;
    font-size: 12px; color: var(--muted); letter-spacing: .2px;
  }
  .lead {
    position: absolute; top: 58px; left: 0; right: 0; margin: 0 auto; width: 580px;
    font-size: 15.6px; line-height: 24px; color: var(--ink);
  }
  .source {
    position: absolute; top: 154px; width: 260px; transform: translateX(-50%);
  }
  .source-icon {
    width: 53px; height: 53px; margin: 0 auto; border: 1px solid var(--line);
    display: flex; align-items: center; justify-content: center;
  }
  .source-title {
    margin-top: 34px; font-size: 12.6px; font-weight: 500;
    letter-spacing: 1.1px; line-height: 19px; text-transform: uppercase;
  }
  .source-years { margin-top: 17px; font-size: 12.4px; color: var(--muted); }
  .feature-colour {
    position: absolute; left: 150px; top: 410px; width: 449px; height: 179px;
    background: linear-gradient(100deg, var(--violet-deep), var(--indigo));
  }
  .feature-photo {
    position: absolute; left: 599px; top: 410px; width: 449px; height: 179px;
    background: linear-gradient(180deg, #a7a39a 0%, var(--sea) 35%, var(--sand) 60%, #6d7b4f 100%);
  }
  .story-card {
    position: absolute; left: 388px; top: 491px; width: 422px; height: 98px;
    background: var(--paper); padding: 56px 0 0 80px;
  }
  .story-title { font-size: 12.6px; font-weight: 500; letter-spacing: .4px; text-transform: uppercase; }
  .story-text { margin-top: 19px; font-size: 12.4px; color: var(--muted); }
</style>
</head>
<body>
<div class="canvas">
  <div class="backdrop" role="img" aria-label="Blurred photograph of a person using a phone, tinted violet to teal"></div>
  <div class="top-band"></div>
  <div class="top-photo" role="img" aria-label="Photograph edge of a person"></div>

  <section class="sources">
    <p class="eyebrow">CROWDSOURCED RESEARCH.</p>
    <p class="lead">Version 1.0 of VELTA Polls merges data from nineteen different survey sources.&nbsp; These are displayed below together with the range of years covered by each source</p>

    <article class="source" style="left:150px">
      <div class="source-icon">
        <svg width="22" height="22" viewBox="0 0 22 22" fill="none" stroke="#9a6ee0" stroke-width="1.2" stroke-linecap="round">
          <circle cx="11" cy="11" r="4.2"/>
          <path d="M11 1.5v3M11 17.5v3M1.5 11h3M17.5 11h3M4.3 4.3l2.1 2.1M15.6 15.6l2.1 2.1M4.3 17.7l2.1-2.1M15.6 6.4l2.1-2.1"/>
        </svg>
      </div>
      <h3 class="source-title">Global Outlook Survey</h3>
      <p class="source-years">1981-2014</p>
    </article>

    <article class="source" style="left:449px">
      <div class="source-icon">
        <svg width="24" height="14" viewBox="0 0 24 14" fill="none" stroke-width="1.3" stroke-linecap="round" stroke-linejoin="round">
          <path d="M6 2L1.5 7 6 12" stroke="#a05ee0"/>
          <path d="M14 1.5L10 12.5" stroke="#7a8fdc"/>
          <path d="M18 2l4.5 5-4.5 5" stroke="#4fc8c2"/>
        </svg>
      </div>
      <h3 class="source-title">Australbarómetro</h3>
      <p class="source-years">1990-2001</p>
    </article>

    <article class="source" style="left:748px">
      <div class="source-icon">
        <svg width="24" height="24" viewBox="0 0 24 24" fill="none" stroke-width="1.3" stroke-linecap="round">
          <circle cx="12" cy="13" r="8.5" stroke="#9a6ee0"/>
          <path d="M12 8.5V13l3 2" stroke="#4fc8c2"/>
          <path d="M3.5 5.5l3-2.5M20.5 5.5l-3-2.5" stroke="#9a6ee0"/>
        </svg>
      </div>
      <h3 class="source-title">Transnational Civic Attitudes Programme</h3>
      <p class="source-years">1985-2016</p>
    </article>
  </section>

  <div class="feature-colour"></div>
  <div class="feature-photo" role="img" aria-label="Photograph of a hiker in a knit hat overlooking a coastal bay"></div>

  <article class="story-card">
    <h3 class="story-title">From the part of beginning</h3>
    <p class="story-text">The ultimate goal is to format every variable</p>
  </article>
</div>
</body>
</html>
```